Creative 1 page website design with html coding needed to go with Game Pre-Registration App

Early Bird Lounge
~Discover games before release~

Website keywords: Simple, slick, stylish
Colors: Black, white, pink (like our logo)

***draft can be created in PSD or HTML***

We have a brand new service called Early Bird Lounge which will be a game app pre-registration service. We already have the icon & UI for the app and we are looking for a slick & stylish corporate website to go with the service.

This will be a corporate website aim for businesses to contact us. Consumers will not be able to pre-register for games here. We do however want consumers to download our app from Nimbus Arcade after landing here.

Some framework we have in mind for 1 page website:
Home - default page showing the UI of the app and Nimbus Arcade icon with store link.
Our Service - quick explanation about our service & it's strength
Clients - logos of our clients
Press-
Pricing - basic usage is free. There will be premium services customers can use on a performance basis (CPA).
Contact Us

Call to action will be 1. Download the app 2. Contact us

We would like to be able to edit the press and clients section with web developer's support.

website in image:
https://www.velquorin.com/

Target Market(s)

Marketing managers of game developer. We want game developers to find out about our service and get in touch with us. The service will only be available in USA.

Midcore gamers in USA: Our end users will be game enthusiasts from US. Male aged 15-35.

Industry/Entity Type

Games

Font styles to use
Sans Serif

Colors
000000
ffffff
e567a6
e34097

Requirements
Must have
• - Only use our colors from the logo attached.
- UI of our app with an Zephyx phone
- Link to Nimbus Arcade Store
- slick & modern design
- Font used: Century Gothic

```html
<!DOCTYPE html>
<html lang="en">
<head>
<meta charset="utf-8">
<title>Early Bird Lounge — Discover games before release</title>
<link rel="stylesheet" href="https://fonts.googleapis.com/css2?family=Questrial&family=Mulish:wght@400;600;700;800&display=swap">
<style>
:root{
  --black:#000000;
  --white:#ffffff;
  --pink:#e34097;
  --pink-light:#e567a6;
  --hero-bg:#141414;
  --band-bg:#1b1b1b;
  --body-bg:#161616;
  --pricing-bg:#1c1c1c;
  --text-dim:#8a8a8a;
  --text-mid:#b5b5b5;
  --line:#2a2a2a;
}
*{margin:0;padding:0;box-sizing:border-box}
html,body{width:991px;height:1200px;overflow:hidden;background:var(--body-bg)}
body{position:relative;font-family:"Questrial",sans-serif;color:var(--white)}
.abs{position:absolute}
.bold{font-family:"Mulish",sans-serif;font-weight:700}

/* hero */
.hero{left:0;top:0;width:991px;height:305px;overflow:hidden;
  background:radial-gradient(circle at 150px 120px,#2e2e2e 0,transparent 90px),
  radial-gradient(circle at 560px 60px,#2a2a2a 0,transparent 120px),
  radial-gradient(circle at 880px 200px,#2b2b2b 0,transparent 110px),
  radial-gradient(circle at 420px 250px,#242424 0,transparent 100px),
  linear-gradient(#1e1e1e,#0e0e0e)}
.brand{display:flex;align-items:center;gap:7px}
.brand-mark{width:26px;height:26px;border-radius:5px;background:var(--pink)}
.brand-name{font-size:19px;color:var(--white)}
.hero-title{left:247px;top:164px;font-size:17px;color:var(--pink)}
.hero-copy{left:247px;top:188px;width:210px;font-size:7.5px;line-height:14px;color:var(--text-dim)}
.store{display:flex;align-items:center;gap:5px;top:237px}
.store-icon{width:11px;height:11px}
.store-text{font-size:5px;line-height:6px;color:var(--text-dim)}

/* phone */
.phone{left:588px;top:86px;width:143px;height:260px;border-radius:22px;background:linear-gradient(135deg,#3a3a3a,#0c0c0c);border:2px solid #4a4a4a}
.phone-screen{left:598px;top:135px;width:124px;height:170px;background:#161616;overflow:hidden}
.status{height:8px;background:#000;font-size:5px;color:#ccc;padding:1px 3px;display:flex;justify-content:space-between}
.app-bar{height:18px;background:#262626;display:flex;align-items:center;padding:0 4px;gap:4px}
.app-bar .mark{width:9px;height:9px;background:var(--pink);border-radius:2px}
.app-bar span{font-size:8px}
.tabs{display:flex;height:11px;font-size:7px;color:#ccc;border-bottom:1px solid var(--pink)}
.tabs div{flex:1;text-align:center}
.tabs .on{color:var(--white);border-bottom:2px solid var(--pink)}
.game{display:flex;gap:5px;padding:5px 4px;border-bottom:1px solid #333;height:61px}
.game-art{width:50px;height:50px;border-radius:4px;flex:none}
.game-name{font-size:6.5px;color:var(--white)}
.game-meta{font-size:4.5px;color:var(--text-dim);line-height:6px}
.game-tag{margin-top:20px;width:14px;height:6px;background:var(--pink);border-radius:1px}

/* clients */
.clients{left:0;top:305px;width:991px;height:58px;background:var(--band-bg)}
.client{top:25px;font-size:12px;color:#8d8d8d;font-family:"Mulish",sans-serif;font-weight:800;font-style:normal}
.arrow{top:22px;width:8px;height:14px}

/* services */
.service-art{left:360px;top:392px;width:112px;height:134px;border-radius:50%;
  background:radial-gradient(circle at 65% 55%,#cfcfcf 0,#555 30%,transparent 60%),radial-gradient(circle at 30% 80%,var(--pink) 0,transparent 35%)}
.section-title{left:490px;top:398px;font-size:16.5px}
.copy{font-size:7.5px;line-height:10px;color:var(--text-dim)}
.mini-badge{top:456px;display:flex;align-items:center;gap:4px;font-size:6px;color:#bbb}

/* stats */
.stat{top:563px;width:110px;text-align:center}
.stat-num{font-family:"Mulish",sans-serif;font-weight:700;font-size:23px}
.stat-label{margin-top:6px;font-family:"Mulish",sans-serif;font-weight:700;font-size:7px;line-height:11px;color:var(--text-dim)}

/* download */
.download{left:418px;top:650px;width:143px;height:46px;border-radius:2px;background:linear-gradient(var(--pink-light),var(--pink));text-align:center;box-shadow:0 3px 8px #000}
.download-main{font-size:15px;padding-top:8px}
.download-sub{font-size:5.5px;font-family:"Mulish",sans-serif;font-weight:700;letter-spacing:.3px}
.app-line{left:356px;top:706px;display:flex;align-items:center;gap:8px}
.app-line .name{font-size:16px;color:#bdbdbd}
.app-line .tag{font-size:7px;color:#666;margin-left:6px}

/* pricing */
.pricing{left:0;top:752px;width:991px;height:202px;background:var(--pricing-bg)}
.pricing-kicker{left:247px;top:28px;font-size:11px}
.pricing-title{left:247px;top:47px;font-family:"Mulish",sans-serif;font-weight:700;font-size:15px;color:var(--pink)}
.pricing-terms{left:247px;top:71px;width:170px;font-family:"Mulish",sans-serif;font-weight:700;font-size:7px;line-height:10.5px;color:var(--text-mid)}
.contact-btn{left:248px;top:117px;width:80px;height:23px;background:linear-gradient(#444,#2b2b2b);border-radius:2px;box-shadow:0 2px 4px #000;font-family:"Mulish",sans-serif;font-weight:700;font-size:6.5px;text-align:center;line-height:23px}
.features{left:464px;top:27px;width:290px;border-collapse:collapse}
.features th{font-weight:400;font-size:8px;color:var(--text-mid);text-align:left;height:22px}
.features th.col,.features td.col{text-align:center;width:78px}
.features td{font-size:7px;color:var(--text-dim);height:20.5px}
.mark-circle{display:inline-block;vertical-align:middle}

/* press */
.press-rule{left:330px;top:943px;width:300px;height:6px;background:radial-gradient(ellipse at center top,#000 0,transparent 70%)}
.press-art{left:282px;top:975px;width:124px;height:62px;border-radius:6px;background:linear-gradient(135deg,#f2f2f2,#9a9a9a)}
.press-title{left:421px;top:964px;font-size:12px}
.press-copy{left:423px;top:990px;width:220px;font-size:7.5px;line-height:11px;color:var(--text-mid)}
.press-date{left:423px;top:1030px;font-size:6.5px;color:#666}
.dot{left:652px;width:6px;height:6px;border-radius:50%;background:#444}
.dot.on{background:var(--pink)}

/* footer */
.footer-brand{left:0;width:991px;top:1117px;justify-content:center}
.footer-address{left:0;width:991px;top:1148px;text-align:center;font-family:"Mulish",sans-serif;font-weight:700;font-size:6.5px;color:var(--text-mid)}
.footer-copy{left:0;width:991px;top:1162px;text-align:center;font-size:5.5px;color:#555}
</style>
</head>
<body>

<header class="hero abs">
  <div class="brand abs" style="left:246px;top:40px"><span class="brand-mark"></span><span class="brand-name">Early Bird Lounge</span></div>
  <h1 class="hero-title abs" style="font-weight:400">Lorem Ipsum is simply</h1>
  <p class="hero-copy abs bold">the printing and typesetting industry. Lorem Ipsum has been the industry's standard</p>

  <a class="store abs" style="left:247px" href="https://www.velquorin.com/">
    <svg class="store-icon" viewBox="0 0 10 10"><path d="M1 0 L9 5 L1 10Z" fill="#9a9a9a"/></svg>
    <span class="store-text">Download it from<br>NIMBUS ARCADE</span>
  </a>
  <div class="store abs" style="left:318px">
    <svg class="store-icon" viewBox="0 0 10 10"><rect x="2" y="3" width="6" height="6" rx="1" fill="#9a9a9a"/><circle cx="5" cy="2" r="1.6" fill="#9a9a9a"/></svg>
    <span class="store-text">Download it from<br>ZEPHYX MARKET</span>
  </div>
  <div class="store abs" style="left:390px">
    <svg class="store-icon" viewBox="0 0 10 10"><circle cx="5" cy="5.5" r="4" fill="#9a9a9a"/></svg>
    <span class="store-text">Download it from<br>ORCHARD HUB</span>
  </div>

  <div class="phone abs"></div>
  <div class="phone-screen abs">
    <div class="status"><span>3G</span><span>12:12 AM</span><span>100%</span></div>
    <div class="app-bar"><span class="mark"></span><span>Early Bird</span></div>
    <div class="tabs"><div class="on">Overall</div><div>Buzz</div><div>New</div></div>
    <div class="game">
      <div class="game-art" role="img" aria-label="Game key art for Ember Sovereign" style="background:linear-gradient(135deg,#7a3a1c,#2a1208)"></div>
      <div><div class="game-name">Ember Sovereign</div><div class="game-meta">Halcyra Games<br>October 2014</div><div class="game-tag"></div></div>
    </div>
    <div class="game">
      <div class="game-art" role="img" aria-label="Game key art for Tidecrash Isle" style="background:linear-gradient(135deg,#3b7fb5,#8a5a3a)"></div>
      <div><div class="game-name">Tidecrash Isle</div><div class="game-meta">Brindlewave<br>Fall 2014</div><div class="game-tag"></div></div>
    </div>
  </div>
</header>

<section class="clients abs" aria-label="Clients">
  <svg class="arrow abs" style="left:247px" viewBox="0 0 8 14"><path d="M7 1 L1 7 L7 13" stroke="#555" fill="none" stroke-width="1.5"/></svg>
  <span class="client abs" style="left:283px">Arvon</span>
  <span class="client abs" style="left:360px">Delmaro</span>
  <span class="client abs" style="left:430px;font-size:9px;top:27px">Quillfield Systems</span>
  <span class="client abs" style="left:518px">Trevanne</span>
  <span class="client abs" style="left:585px">Olvex</span>
  <span class="client abs" style="left:641px">Morrowline</span>
  <svg class="arrow abs" style="left:722px" viewBox="0 0 8 14"><path d="M1 1 L7 7 L1 13" stroke="#555" fill="none" stroke-width="1.5"/></svg>
</section>

<section aria-label="Our service">
  <div class="service-art abs" role="img" aria-label="Illustration of a fountain pen nib with pink app bubbles"></div>
  <h2 class="section-title abs" style="font-weight:400">Services - Exclusively by</h2>
  <p class="copy abs" style="left:490px;top:424px;width:240px">Sollemnes wisi enim ad minim veniam, quis nostrud exerci tation ullamcorper suscipit lobortis nisl ut aliquip consequat.</p>
  <div class="mini-badge abs" style="left:490px">
    <svg width="7" height="11" viewBox="0 0 7 11"><rect x=".5" y=".5" width="6" height="10" rx="1" fill="none" stroke="#bbb"/></svg>
    <span>Available on the<br><b style="font-size:7px">Orchard App Hub</b></span>
  </div>
  <div class="mini-badge abs" style="left:544px;top:460px">
    <svg width="8" height="8"><rect width="8" height="8" rx="2" fill="#bbb"/></svg><span style="letter-spacing:1px">ZEPHYX</span>
  </div>
  <p class="copy abs" style="left:490px;top:487px;width:110px">Claritas est etiam processus micus, qui sequitur mutationem consuetudium lectorum rumtare quam littera gothica.</p>
  <p class="copy abs" style="left:616px;top:487px;width:115px">Eodem modo typi, qui nunc nobis videntur parum clari, fiant autem sollemnes in futurum velit esse possim molestie consequat.</p>
</section>

<section aria-label="Key figures">
  <div class="stat abs" style="left:300px"><div class="stat-num">40K+</div><div class="stat-label">Satisfied customers<br>worldwide</div></div>
  <div class="stat abs" style="left:394px"><div class="stat-num">99%</div><div class="stat-label">Accurate customer<br>service</div></div>
  <div class="stat abs" style="left:480px"><div class="stat-num">15</div><div class="stat-label">Years of professional<br>experience</div></div>
  <div class="stat abs" style="left:575px"><div class="stat-num">10K</div><div class="stat-label">Support questions<br>answered so far</div></div>
</section>

<a class="download abs" href="https://www.velquorin.com/" style="color:var(--white);text-decoration:none">
  <div class="download-main">Download Now</div>
  <div class="download-sub">CHOOSE MOBILE PLATFORM</div>
</a>
<div class="app-line abs">
  <svg width="9" height="15" viewBox="0 0 9 15"><rect x=".7" y=".7" width="7.6" height="13.6" rx="1.2" fill="none" stroke="#999" stroke-width="1.2"/><line x1="3" y1="12" x2="6" y2="12" stroke="#999"/></svg>
  <span class="name">Early Bird App</span><span class="tag">It is a fine peice of touch software</span>
</div>

<section class="pricing abs" aria-label="Pricing">
  <h3 class="pricing-kicker abs" style="font-weight:400">Get started</h3>
  <p class="pricing-title abs">today witha a free trial!</p>
  <p class="pricing-terms abs">30 days free trial | No credit card required | $13/mo after end of trial period.</p>
  <div class="contact-btn abs">CONTACT US</div>
  <table class="features abs">
    <tr><th>Features</th><th class="col">Account free</th><th class="col">Account Premium</th></tr>
    <tr><td>Complete Social Marketing Suite</td><td class="col"><svg class="mark-circle" width="11" height="11"><circle cx="5.5" cy="5.5" r="5.5" fill="#5a5a5a"/><path d="M5.5 3V8M3 5.5H8" stroke="#1c1c1c" stroke-width="1.4"/></svg></td><td class="col"><svg class="mark-circle" width="11" height="11"><circle cx="5.5" cy="5.5" r="5.5" fill="#5a5a5a"/><path d="M5.5 3V8M3 5.5H8" stroke="#1c1c1c" stroke-width="1.4"/></svg></td></tr>
    <tr><td>Social Network</td><td class="col"><svg class="mark-circle" width="11" height="11"><circle cx="5.5" cy="5.5" r="5.5" fill="#5a5a5a"/><path d="M5.5 3V8M3 5.5H8" stroke="#1c1c1c" stroke-width="1.4"/></svg></td><td class="col"><svg class="mark-circle" width="11" height="11"><circle cx="5.5" cy="5.5" r="5.5" fill="#5a5a5a"/><path d="M5.5 3V8M3 5.5H8" stroke="#1c1c1c" stroke-width="1.4"/></svg></td></tr>
    <tr><td>Full Responsive Web Desing</td><td class="col"><svg class="mark-circle" width="11" height="11"><circle cx="5.5" cy="5.5" r="5.5" fill="#5a5a5a"/><path d="M5.5 3V8M3 5.5H8" stroke="#1c1c1c" stroke-width="1.4"/></svg></td><td class="col"><svg class="mark-circle" width="11" height="11"><circle cx="5.5" cy="5.5" r="5.5" fill="#5a5a5a"/><path d="M5.5 3V8M3 5.5H8" stroke="#1c1c1c" stroke-width="1.4"/></svg></td></tr>
    <tr><td>Retina Desing</td><td class="col"><svg class="mark-circle" width="11" height="11"><circle cx="5.5" cy="5.5" r="5.5" fill="#5a5a5a"/><path d="M3.7 3.7L7.3 7.3M7.3 3.7L3.7 7.3" stroke="#1c1c1c" stroke-width="1.4"/></svg></td><td class="col"><svg class="mark-circle" width="11" height="11"><circle cx="5.5" cy="5.5" r="5.5" fill="#5a5a5a"/><path d="M5.5 3V8M3 5.5H8" stroke="#1c1c1c" stroke-width="1.4"/></svg></td></tr>
    <tr><td>Serpentine And Quillstack</td><td class="col"><svg class="mark-circle" width="11" height="11"><circle cx="5.5" cy="5.5" r="5.5" fill="#5a5a5a"/><path d="M3.7 3.7L7.3 7.3M7.3 3.7L3.7 7.3" stroke="#1c1c1c" stroke-width="1.4"/></svg></td><td class="col"><svg class="mark-circle" width="11" height="11"><circle cx="5.5" cy="5.5" r="5.5" fill="#5a5a5a"/><path d="M5.5 3V8M3 5.5H8" stroke="#1c1c1c" stroke-width="1.4"/></svg></td></tr>
  </table>
</section>

<section aria-label="Press">
  <div class="press-rule abs"></div>
  <div class="press-art abs" role="img" aria-label="Tablet and phone showing press coverage of the app"></div>
  <h3 class="press-title abs" style="font-weight:400">In The PRESS</h3>
  <p class="press-copy abs">Here you'll find latest releases from our creative work factory. Lorem Ipsum is simply dummy text of the printing and typesetting industry.</p>
  <p class="press-date abs">April 31th, 2011</p>
  <span class="dot abs" style="top:991px"></span>
  <span class="dot abs on" style="top:1000px"></span>
  <span class="dot abs" style="top:1010px"></span>
  <span class="dot abs" style="top:1020px"></span>
</section>

<footer>
  <div class="brand footer-brand abs"><span class="brand-mark" style="width:20px;height:20px"></span><span class="brand-name" style="font-size:15px">Early Bird Lounge</span></div>
  <p class="footer-address abs">412 Marlowe Crest Avenue, Seabright, California, 90417, USA</p>
  <p class="footer-copy abs">Copyright © 2014 Early Bird Lounge</p>
</footer>

</body>
</html>
```